Letterhead & Business Card Design Project

Use existing logo to create a new letterhead and business card design. Looking for something clean modern using color options of black, white and gray. The green from the logo may be used lightly as an accent color.

Target Market(s)

Professional business people

Industry/Entity Type

Business

Requirements
Must have
• Business card with front and back design using existing logo.
Nice to have
• Professional presentation
Clean look
Should not have
• No oil rigs, pumpjacks or clip art.

```html
<!DOCTYPE html>
<html lang="en">
<head>
<meta charset="utf-8">
<title>Halvor Exploration – Business Card</title>
<link href="https://fonts.googleapis.com/css2?family=Mulish:wght@400;600;700&display=swap" rel="stylesheet">
<style>
  :root {
    --stage: #4b4b4b;
    --card-dark: #070707;
    --card-light: #f3f3f3;
    --ink: #111111;
    --ink-soft: #2a2a2a;
    --paper-text: #e8e8e8;
    --muted: #9a9a9a;
    --accent: #2fa82f;
  }
  * { box-sizing: border-box; margin: 0; padding: 0; }
  html, body { width: 1200px; height: 1000px; overflow: hidden; }
  body {
    background: var(--stage);
    font-family: "Mulish", "Helvetica Neue", Arial, sans-serif;
    position: relative;
  }
  .card {
    position: absolute;
    width: 528px;
    height: 301px;
    border-radius: 14px;
  }
  .card-back { left: 207px; top: 165px; background: var(--card-dark); }
  .card-front { left: 473px; top: 550px; background: var(--card-light); color: var(--ink); }

  .wordmark {
    font-family: "Mulish", "Helvetica Neue", Arial, sans-serif;
    font-weight: 400;
    letter-spacing: 4px;
    text-transform: uppercase;
    white-space: nowrap;
  }
  .card-back .wordmark {
    position: absolute; left: 0; right: 0; top: 68px;
    text-align: center; font-size: 26px; color: var(--paper-text);
  }
  .card-front .wordmark {
    position: absolute; right: 36px; top: 58px;
    font-size: 24px; color: var(--ink);
  }

  .site-url {
    position: absolute; left: 0; right: 0; top: 246px;
    text-align: center; font-size: 13px; color: var(--paper-text);
  }
  .site-url .domain { color: var(--accent); }

  .person { position: absolute; left: 31px; top: 155px; }
  .person-name { font-size: 17px; font-weight: 700; }
  .person-title { font-size: 12px; color: var(--ink-soft); margin-top: 2px; }

  .contact-lines {
    position: absolute; left: 31px; top: 226px;
    font-size: 12px; line-height: 15.5px; color: var(--ink-soft);
  }
  .contact-lines .label { color: var(--accent); }
  .divider {
    position: absolute; left: 182px; top: 226px;
    width: 2px; height: 46px; background: var(--accent);
  }
  .address-lines {
    position: absolute; left: 216px; top: 226px;
    font-size: 12px; line-height: 15.5px; color: var(--ink-soft);
  }
</style>
</head>
<body>
  <section class="card card-back">
    <div class="wordmark">Halvor Exploration</div>
    <p class="site-url">www.<span class="domain">halvorexploration</span>.com</p>
  </section>

  <section class="card card-front">
    <div class="wordmark">Halvor Exploration</div>
    <div class="person">
      <p class="person-name">Daniel R Hayes</p>
      <p class="person-title">Managing Member</p>
    </div>
    <div class="contact-lines">
      <p><span class="label">Phone:</span> 555.204.7130</p>
      <p><span class="label">Cell:</span> 555.318.2964</p>
      <p><span class="label">Fax:</span> 555.204.7131</p>
    </div>
    <div class="divider"></div>
    <div class="address-lines">
      <p>4120 North Cedar Ave Suite 210</p>
      <p>Fairview, Kansas 66042</p>
      <p>www.halvorexploration.com</p>
    </div>
  </section>
</body>
</html>
```